Menu Design for Indian Restaurant

We are a new Indian restaurant, named Spices of Sarani Restaurant, looking for a sophisticated looking menu. It is a semi-formal dining restaurant with wooden tables and chairs and will have a focus on a creating a lively atmosphere. Environment-friendly products will be used, and the menu will be 100% vegetarian. There will be an emphasis on fresh, healthy and delicious food. We will be targeting vegans, vegetarians, health conscious people, people from all age groups, Indians, Australian's as well as other ethnic communities. We need a clean, simple, sophisticated design for the new restaurant menu. Attached is the restaurant logo for reference.

UPDATE:
- We have attached the menu
- We are not looking for any particular type of layout or size (open to suggests). Please suggest this after having a look at the menu contents. However, we will be having one formal menu to be used in the restaurant, and one in brochure form for distribution.
- There are no images at present. If you feel the need of images, please use sample images for now.

Thank you for the entries thus far.
Updates

Target Market(s)

All age groups from different nationalities

Industry/Entity Type

Indian Restaurant

Colors

Designer to choose colors to be used in the design.

Requirements
Nice to have
• This will be printed on environmentally friendly paper.

```html
<!DOCTYPE html>
<html lang="en">
<head>
<meta charset="utf-8">
<title>Spices of Sarani Restaurant – Menu Pages 10 &amp; 11</title>
<link rel="stylesheet" href="https://fonts.googleapis.com/css2?family=Alegreya+Sans:wght@500;700&family=Open+Sans:ital,wght@1,800&display=swap">
<style>
  :root {
    --saffron: #f58a3a;
    --saffron-soft: #f7a066;
    --green: #17a05a;
    --green-soft: #63cc95;
    --brush-orange: #f6993a;
    --brush-green: #178a45;
    --ink: #222222;
    --desc: #b8703a;
    --ribbon-dark: #3a2a24;
    --page-edge: #8a8a8a;
    --label: #333333;
  }
  html, body {
    margin: 0;
    padding: 0;
    width: 1200px;
    height: 1158px;
    overflow: hidden;
    background: #ffffff;
  }
  .stage {
    position: relative;
    width: 1500px;
    height: 1448px;
    transform: scale(0.8);
    transform-origin: 0 0;
    font-family: "Alegreya Sans", sans-serif;
    font-variant-numeric: oldstyle-nums;
  }
  .page {
    position: absolute;
    top: 0;
    width: 727px;
    height: 1400px;
    box-sizing: border-box;
    border: 1px solid var(--page-edge);
    overflow: hidden;
    background: #ffffff;
  }
  .page--left { left: 0; }
  .page--right { left: 773px; }
  .page-frame {
    position: absolute;
    left: 0; top: 0;
    width: 727px;
    height: 1400px;
  }
  .ribbon {
    position: absolute;
    left: 73px;
    height: 38px;
    box-shadow: 0 5px 4px -2px rgba(0,0,0,0.35);
  }
  .ribbon__bar {
    position: absolute;
    inset: 0 20px 0 0;
    background: var(--saffron);
  }
  .ribbon__notch {
    position: absolute;
    left: 0; top: 0;
    width: 22px; height: 38px;
    background: var(--ribbon-dark);
    clip-path: polygon(0 0, 100% 50%, 0 100%);
  }
  .ribbon__tip {
    position: absolute;
    right: 0; top: 0;
    width: 22px; height: 38px;
    background: var(--ribbon-dark);
    clip-path: polygon(0 0, 60% 0, 100% 50%, 60% 100%, 0 100%);
  }
  .ribbon__title {
    position: absolute;
    left: 42px; top: 0;
    line-height: 38px;
    font-family: "Open Sans", sans-serif;
    font-style: italic;
    font-weight: 800;
    font-size: 25px;
    letter-spacing: -0.3px;
    color: #ffffff;
    white-space: nowrap;
  }
  .item, .desc, .price {
    position: absolute;
    white-space: nowrap;
  }
  .item {
    font-size: 21px;
    font-weight: 500;
    line-height: 24px;
    color: var(--ink);
  }
  .desc {
    font-size: 15px;
    font-weight: 700;
    line-height: 20px;
    color: var(--desc);
  }
  .price {
    font-size: 20px;
    font-weight: 700;
    line-height: 24px;
    color: var(--ink);
    text-align: right;
  }
  .page--left .item, .page--left .desc { left: 72px; }
  .page--left .price { right: 59px; }
  .page--right .item { left: 73px; }
  .page--right .price { right: 75px; }
  .page-label {
    position: absolute;
    top: 1412px;
    width: 727px;
    text-align: center;
    font-family: Arial, Helvetica, sans-serif;
    font-weight: 700;
    font-size: 38px;
    line-height: 46px;
    color: var(--label);
  }
</style>
</head>
<body>
<div class="stage">

  <!-- Page 10 -->
  <section class="page page--left">
    <svg class="page-frame" viewBox="0 0 727 1400" xmlns="http://www.w3.org/2000/svg">
      <defs>
        <linearGradient id="topWash10" x1="0" y1="0" x2="0" y2="1">
          <stop offset="0" stop-color="#f7a066"/>
          <stop offset="1" stop-color="#ffffff"/>
        </linearGradient>
        <linearGradient id="bottomWash10" x1="0" y1="0" x2="0" y2="1">
          <stop offset="0" stop-color="#ffffff"/>
          <stop offset="1" stop-color="#63cc95"/>
        </linearGradient>
      </defs>
      <rect x="0" y="0" width="727" height="370" fill="url(#topWash10)" role="img" aria-label="Floral paisley ornament pattern in saffron tones"/>
      <rect x="0" y="1090" width="727" height="310" fill="url(#bottomWash10)"/>
      <path d="M38,1358 L38,480 C70,460 75,400 30,385 C10,330 40,300 120,300 C100,230 160,180 230,190 C230,140 330,120 363,80 C396,120 496,140 496,190 C566,180 626,230 606,300 C686,300 716,330 696,385 C651,400 656,460 688,480 L688,1358 Z" fill="#ffffff"/>
      <path d="M38,862 L38,480 C70,460 75,400 30,385 C10,330 40,300 120,300 C100,230 160,180 230,190 C230,140 330,120 363,80 C396,120 496,140 496,190 C566,180 626,230 606,300 C686,300 716,330 696,385 C651,400 656,460 688,480 L688,675" fill="none" stroke="var(--saffron)" stroke-width="5"/>
      <path d="M38,893 L38,1358 L688,1358 L688,703" fill="none" stroke="var(--green)" stroke-width="5"/>
      <rect x="208" y="252" width="312" height="70" rx="30" fill="var(--brush-orange)" role="img" aria-label="Saffron brush stroke"/>
      <rect x="208" y="370" width="312" height="70" rx="30" fill="var(--brush-green)" role="img" aria-label="Green brush stroke"/>
    </svg>

    <div class="ribbon" style="top:493px;width:357px"><span class="ribbon__bar"></span><span class="ribbon__notch"></span><span class="ribbon__tip"></span><span class="ribbon__title">SARANI BANQUET</span></div>
    <div class="item" style="top:565px;left:67px">Banquet for 4/6/8/12/24 people</div>
    <div class="price" style="top:567px">24.9</div>
    <div class="desc" style="top:590px;left:67px">2 entrée, 4 mains, one rice, naan/ roti, pappadam, salad, riata</div>
    <div class="desc" style="top:610px;left:67px">One dessert of your choice</div>

    <div class="ribbon" style="top:663px;width:357px"><span class="ribbon__bar"></span><span class="ribbon__notch"></span><span class="ribbon__tip"></span><span class="ribbon__title">THALI</span></div>
    <div class="item" style="top:741px">Gujrati Thali</div>
    <div class="price" style="top:742px">21.9</div>
    <div class="desc" style="top:774px">4 curry salad pickle rice yogurt 2 roti pappadam sweet</div>
    <div class="item" style="top:805px">Temil Thali</div>
    <div class="price" style="top:806px">21.9</div>
    <div class="desc" style="top:838px">4 curry salad pickle rice yogurt 2 roti pappadam sweet</div>
    <div class="item" style="top:869px">Punjabi Thali</div>
    <div class="price" style="top:871px">21.9</div>
    <div class="desc" style="top:902px">4 curry salad pickle rice yogurt naan pappadam sweet</div>

    <div class="ribbon" style="top:986px;width:357px"><span class="ribbon__bar"></span><span class="ribbon__notch"></span><span class="ribbon__tip"></span><span class="ribbon__title">FLAVOURS OF RICE</span></div>
    <div class="item" style="top:1063px">Chitranna</div>
    <div class="price" style="top:1065px">4.9</div>
    <div class="desc" style="top:1096px">Basmati rice mustard seeds red chilli curry leafs lemon and coconut</div>
    <div class="desc" style="top:1116px">flavoured</div>
    <div class="item" style="top:1147px">Pulao Rice</div>
    <div class="price" style="top:1136px">4.9</div>
    <div class="desc" style="top:1180px">Cumin bay leaf pepper corn cinnamon flavoured</div>
    <div class="item" style="top:1211px">Steamed Basmati Rice</div>
    <div class="price" style="top:1208px">3.9</div>
    <div class="desc" style="top:1244px">Basmati rice no gluten less starch</div>
    <div class="item" style="top:1276px">Vegetable Biryani</div>
    <div class="price" style="top:1278px">15.9</div>
    <div class="desc" style="top:1308px">Seasonal vegetable cooked with basmati rice and Indian aroma spice</div>
  </section>
  <div class="page-label" style="left:12px">PAGE 10</div>

  <!-- Page 11 -->
  <section class="page page--right">
    <svg class="page-frame" viewBox="0 0 727 1400" xmlns="http://www.w3.org/2000/svg">
      <defs>
        <linearGradient id="topWash11" x1="0" y1="0" x2="0" y2="1">
          <stop offset="0" stop-color="#f7a066"/>
          <stop offset="1" stop-color="#ffffff"/>
        </linearGradient>
        <linearGradient id="bottomWash11" x1="0" y1="0" x2="0" y2="1">
          <stop offset="0" stop-color="#ffffff"/>
          <stop offset="1" stop-color="#63cc95"/>
        </linearGradient>
      </defs>
      <rect x="0" y="0" width="727" height="370" fill="url(#topWash11)" role="img" aria-label="Floral paisley ornament pattern in saffron tones"/>
      <rect x="0" y="1090" width="727" height="310" fill="url(#bottomWash11)"/>
      <path d="M38,1358 L38,480 C70,460 75,400 30,385 C10,330 40,300 120,300 C100,230 160,180 230,190 C230,140 330,120 363,80 C396,120 496,140 496,190 C566,180 626,230 606,300 C686,300 716,330 696,385 C651,400 656,460 688,480 L688,1358 Z" fill="#ffffff"/>
      <path d="M38,866 L38,480 C70,460 75,400 30,385 C10,330 40,300 120,300 C100,230 160,180 230,190 C230,140 330,120 363,80 C396,120 496,140 496,190 C566,180 626,230 606,300 C686,300 716,330 696,385 C651,400 656,460 688,480 L688,675" fill="none" stroke="var(--saffron)" stroke-width="5"/>
      <path d="M38,893 L38,1358 L688,1358 L688,703" fill="none" stroke="var(--green)" stroke-width="5"/>
      <rect x="208" y="252" width="312" height="70" rx="30" fill="var(--brush-orange)" role="img" aria-label="Saffron brush stroke"/>
      <rect x="208" y="370" width="312" height="70" rx="30" fill="var(--brush-green)" role="img" aria-label="Green brush stroke"/>
    </svg>

    <div class="ribbon" style="top:493px;width:504px"><span class="ribbon__bar"></span><span class="ribbon__notch"></span><span class="ribbon__tip"></span><span class="ribbon__title">TAWA BREADS &amp; TANDOORI BREAD</span></div>
    <div class="item" style="top:565px">Chappati</div><div class="price" style="top:566px">1.9</div>
    <div class="item" style="top:598px">Roti</div><div class="price" style="top:599px">2.9</div>
    <div class="item" style="top:630px">Naan</div><div class="price" style="top:632px">3.9</div>
    <div class="item" style="top:663px">Garlic Naan</div><div class="price" style="top:665px">3.9</div>
    <div class="item" style="top:696px">Butter Naan</div><div class="price" style="top:698px">4.9</div>
    <div class="item" style="top:729px">Aloo Kulcha</div><div class="price" style="top:731px">4.9</div>
    <div class="item" style="top:762px">Paneer Kulcha</div><div class="price" style="top:764px">5.9</div>
    <div class="item" style="top:795px">Kashmiri Naan</div><div class="price" style="top:796px">5.9</div>
    <div class="item" style="top:828px">Missi Roti</div><div class="price" style="top:829px">3.9</div>
    <div class="item" style="top:861px">Makki Ki Roti</div><div class="price" style="top:862px">3.9</div>

    <div class="ribbon" style="top:950px;width:504px"><span class="ribbon__bar"></span><span class="ribbon__notch"></span><span class="ribbon__tip"></span><span class="ribbon__title">ACCOMPANIMENTS</span></div>
    <div class="item" style="top:1022px">Kachumber Salad</div><div class="price" style="top:1023px">3.9</div>
    <div class="item" style="top:1057px">Green Salad</div><div class="price" style="top:1059px">4.9</div>
    <div class="item" style="top:1093px">Onion Salad</div><div class="price" style="top:1094px">3.9</div>
    <div class="item" style="top:1129px">Raita Cucumber</div><div class="price" style="top:1130px">3.9</div>
    <div class="item" style="top:1164px">Raita Cucumber Carrots</div><div class="price" style="top:1166px">3.9</div>
    <div class="item" style="top:1200px">Pickle</div><div class="price" style="top:1201px">2.9</div>
    <div class="item" style="top:1236px">Mango Chutney</div><div class="price" style="top:1237px">3.9</div>
    <div class="item" style="top:1271px">Pappadam South (2pcs)</div><div class="price" style="top:1272px">1.9</div>
    <div class="item" style="top:1307px">Paddam Black Pepper (2pcs)</div><div class="price" style="top:1308px">1.9</div>
  </section>
  <div class="page-label" style="left:785px">PAGE 11</div>

</div>
</body>
</html>
```